Old Mills Along the Whitebrook Vale

We need a cover for a regional book "Die Mühlen am Weißen Bach". The book is about the region frankonia in southern Germany and about the history of electricity in from 1900 to now. The cover should have some regional reference and some reference to electric power. It contains history and stories about electricity.

Reason: We have to wait for the opinion of the publisher.

Target Market(s)

Adults based in southern Germany who are interested in local history and electricity

Requirements
Must have
• Regional reference to franconia (Region in southern Germany) and reference to electricity.
Nice to have
• The files are just some examples for regional pictures, they are not necessary.

```html
<!DOCTYPE html>
<html lang="de">
<head>
<meta charset="utf-8">
<title>Die Mühlen am Weißen Bach – Buchumschlag</title>
<link rel="stylesheet" href="https://fonts.googleapis.com/css2?family=Bodoni+Moda:ital,wght@0,400;1,400&family=Open+Sans:wght@400&display=swap">
<style>
  :root {
    --cover-red: #7e141e;
    --title-red: #7f1620;
    --paper: #ffffff;
    --ink: #2b2b2b;
    --type-light: #ffffff;
  }
  * { margin: 0; padding: 0; box-sizing: border-box; }
  html, body { width: 1200px; height: 802px; overflow: hidden; background: var(--paper); }
  .cover {
    position: relative; width: 1200px; height: 802px;
    background: var(--paper); font-family: "Bodoni Moda", serif;
  }
  .back-cover {
    position: absolute; left: 0; top: 0; width: 626px; height: 802px;
    background: var(--cover-red);
  }
  .back-photo {
    position: absolute; left: 106px; top: 218px; width: 332px; height: 247px;
    background:
      linear-gradient(90deg, rgba(40,60,30,0.35) 0%, rgba(0,0,0,0) 25%, rgba(0,0,0,0) 75%, rgba(60,90,30,0.35) 100%),
      linear-gradient(180deg, #a9c2d8 0%, #c9d6df 30%, #c6cac8 45%, #9aa3a2 52%, #3f5a2c 60%, #4b7a2e 66%, #5d9a3a 80%, #4f8a32 100%);
  }
  .spine-title, .spine-author {
    position: absolute; left: 596px; color: var(--type-light);
    font-size: 16px; letter-spacing: 0.2px; white-space: nowrap;
    transform-origin: 0 0; transform: rotate(90deg);
  }
  .spine-title { top: 40px; }
  .spine-author { top: 604px; font-size: 17px; }

  .front-photos {
    position: absolute; left: 626px; top: 0; width: 574px; height: 698px;
    display: flex;
  }
  .photo-strip { flex: 1; height: 100%; }
  .strip-town {
    background: linear-gradient(180deg, #e2e2e2 0%, #a8a8a8 18%, #6e6e6e 40%, #4a4a4a 58%, #3a3a3a 72%, #7a7a7a 88%, #9c9c9c 100%);
  }
  .strip-wind {
    background: linear-gradient(180deg, #0a3a8c 0%, #1553a8 40%, #3f78c4 64%, #c9dbef 76%, #eef3f8 84%, #b8c6d8 93%, #8a8f96 100%);
  }
  .strip-portrait {
    background: linear-gradient(180deg, #d8d8d8 0%, #f0f0f0 12%, #bdbdbd 24%, #8a8a8a 32%, #2e2e2e 62%, #1e1e1e 100%);
  }
  .strip-fountain {
    background: linear-gradient(180deg, #2d6fbd 0%, #3a78c0 26%, #4a6a6a 36%, #8b8676 58%, #c8c0ae 72%, #a39c8a 88%, #d0cbbd 100%);
  }
  .strip-tower {
    background:
      linear-gradient(90deg, rgba(0,0,0,0) 0%, rgba(0,0,0,0) 28%, rgba(235,240,250,0.85) 36%, rgba(235,240,250,0.85) 66%, rgba(0,0,0,0) 74%),
      linear-gradient(180deg, #1c4aa6 0%, #3a66c2 50%, #23376c 80%, #0e1630 100%);
  }

  .title-block {
    position: absolute; left: 716px; top: 227px; width: 386px; height: 202px;
    background: var(--title-red); color: var(--type-light);
    display: flex; flex-direction: column; justify-content: center; align-items: center;
  }
  .book-title {
    font-weight: 400; font-size: 52px; line-height: 60px;
    letter-spacing: 3px; text-align: center; text-transform: uppercase;
  }
  .subtitle-band {
    position: absolute; left: 716px; top: 432px; width: 386px; height: 32px;
    background: var(--title-red); color: var(--type-light);
    font-family: "Open Sans", sans-serif; font-size: 15.5px; letter-spacing: 0.2px;
    display: flex; align-items: center; justify-content: center; text-transform: uppercase;
  }
  .front-footer {
    position: absolute; left: 626px; top: 698px; width: 574px; height: 104px;
    text-align: center; color: var(--ink);
  }
  .tagline { font-style: italic; font-size: 16px; margin-top: 15px; letter-spacing: 0.3px; }
  .author { font-size: 17px; margin-top: 11px; letter-spacing: 0.6px; }
</style>
</head>
<body>
<div class="cover">
  <section class="back-cover">
    <div class="back-photo" role="img" aria-label="Foto: Kraftwerk mit Schornstein, Kühltürmen und Strommasten hinter einer grünen Wiese"></div>
    <div class="spine-title">Die Mühlen am Weißen Bach - von der Kaiserzeit bis zur Energiewende</div>
    <div class="spine-author">Von Konrad Weiler</div>
  </section>

  <section class="front-photos">
    <div class="photo-strip strip-town" role="img" aria-label="Schwarzweißfoto: fränkisches Giebelhaus in der Altstadt mit Straßenlaterne"></div>
    <div class="photo-strip strip-wind" role="img" aria-label="Foto: Windrad vor blauem Himmel und Wolken"></div>
    <div class="photo-strip strip-portrait" role="img" aria-label="Schwarzweißfoto: Ausschnitt eines historischen Porträts"></div>
    <div class="photo-strip strip-fountain" role="img" aria-label="Foto: fränkische Brunnenfigur mit Fahne und verziertem Steinsockel"></div>
    <div class="photo-strip strip-tower" role="img" aria-label="Foto: weißer Kraftwerksschornstein vor blauem Himmel"></div>
  </section>

  <div class="title-block">
    <h1 class="book-title">Die Mühlen<br>am Weissen<br>Bach</h1>
  </div>
  <div class="subtitle-band">Von der Kaiserzeit bis zur Energiewende</div>

  <footer class="front-footer">
    <p class="tagline">Geschichte, Geschichten und Strom</p>
    <p class="author">Von Konrad Weiler</p>
  </footer>
</div>
</body>
</html>
```